Flyer Design Project

*Update* Would also be interested to see designs in landscape format too.
My company is Brackley Van Hire Limited. A self drive van hire company based in Essex.
I need a double sided A5 flyer design to target new business customers both small and large. The flyer will be printed on 350-400gsm.
Our website is www.brackleyvanhire-example.com this will give you an idea of our colour scheme.
The purpose of the flyer is to make companies aware of our business and what we offer and to ideally either make contact with us immediatly or at least retain the flyer so that they use us in future. Our aim is that when they require van hire they think of us first.
In terms of design it needs to be proffessional, eye catching, informative and memorable.
I would like the 4 main van types we supply to be on the leaflet. ideally side views. Probably stock images with our graphics placed on them. I'm sure as a designer you will have a fair idea of what I'm talking about. The van types are Carvel compact, Carvel SWB, Carvel LWB high roof and Carvel luton.
Our facebook page may also help (pictures of some of our vans are here)...
http://www.facebook.com/pages/Brackley-Van-Hire/509362847105
Ideally it will include the following. The layout of the content however I am happy to leave to the designer...
(title) Low cost business van hire
Throughout Essex and Herts including Harlow, Epping, Hoddesdon, Bishops Stortford and Hertford
We have vans in all sizes including Luton tail lifts for short and long term rental on flexible terms for any purpose at very competitive prices.
Open 7 days
Short or long term rental on daily, weekly or monthly payment terms
No charges for additional drivers
Unlimited mileage allowance
24/7 online booking facility
Account facilities available
Secure customer parking
Out of hours drop off facility
(maybe use tick boxes for the above?)
When you need a van for business purposes give Brackley a call first.
We supply vans to businesses throughout Herts and Essex from large blue chip multinationals to small self employed tradesman. We understand the requirements of business customers and provide a low cost, flexible, efficient van hire solution regardless of the size of your business.
We’re cheaper than the rest
We regularly search the market to ensure our pricing is always competitive. It's important to us to give you excellent value for money. We operate a clear pricing structure with no hidden extras. Call us now and let us give you a quote.
Short or long term van hire
We can supply vans according to your needs from just a single days rental to long term contract rental for 1 month, 6 months, a whole year or more.
Committed to Customer service
We take customer service very seriously. We want you to be delighted each and every time you use us. That’s why We’ll always go out of our way to give you a first class service.
The longer you hire the cheaper it gets with discounts of up to 70% on our daily rental rates. (maybe in speech type bubble or highlighted in some way?)
Flyer needs:
Map of our location and address
- Finding us is easy, we're located in the marlowe industrial estate in Harlow
42 Dunmore Court
Harlow
Essex
CM17 2QX
Telephone number
0800 07 316 94
Website address
www.brackleyvanhire-example.com
Logo
attached
Testimonial?
Can supply
www.brackleyvanhire-example.com
0800 07 316 94

```html
<!DOCTYPE html>
<html lang="en">
<head>
<meta charset="utf-8">
<title>Brackley Van Hire – Business Flyer</title>
<link href="https://fonts.googleapis.com/css2?family=Arimo:ital,wght@0,400;0,700;1,400;1,700&display=swap" rel="stylesheet">
<style>
  :root {
    --green-dark: #4c8f3c;
    --green-mid: #6aa957;
    --green-light: #9fd08a;
    --green-bright: #66cc00;
    --paper: #ffffff;
    --ink: #111111;
    --frame: #9a9a9a;
    --map-land: #e9e7e1;
    --map-road: #f4b63f;
  }
  * { margin: 0; padding: 0; box-sizing: border-box; }
  html, body { width: 1200px; height: 846px; overflow: hidden; background: #fff; }
  .flyer {
    position: relative;
    width: 1200px; height: 846px;
    border: 1px solid var(--frame);
    background: linear-gradient(to bottom, var(--paper) 0%, var(--paper) 40%, #d7f0b8 62%, #9ee04e 82%, var(--green-bright) 100%);
    font-family: "Arimo", Arial, sans-serif;
    color: var(--ink);
    overflow: hidden;
  }
  .banners { position: absolute; inset: 0; }
  .banner-text {
    position: absolute;
    left: 52px; width: 748px;
    text-align: center;
    color: #fff;
    font-size: 28px;
    line-height: 32px;
  }
  .banner-text.top { top: 41px; }
  .banner-text.bottom { top: 722px; }
  .intro {
    position: absolute; left: 87px; width: 710px;
    font-size: 17.5px; line-height: 24px;
  }
  .intro p + p { margin-top: 12px; }
  .intro { top: 153px; }
  .feature { position: absolute; left: 36px; width: 760px; }
  .feature .icon { position: absolute; left: 0; top: -8px; width: 50px; height: 34px; }
  .feature h2 {
    margin-left: 51px;
    font-size: 17.5px; font-weight: 700; font-style: italic;
    text-decoration: underline; line-height: 24px;
  }
  .feature p { margin-left: 51px; font-size: 17.5px; line-height: 24.5px; }
  .f1 { top: 339px; } .f2 { top: 486px; } .f3 { top: 584px; }
  .address {
    position: absolute; right: 58px; top: 90px;
    text-align: right; font-size: 32px; line-height: 40px;
  }
  .address .phone { font-size: 30px; }
  .web {
    position: absolute; right: 52px; top: 284px;
    font-size: 33px; letter-spacing: -0.5px;
  }
  .map {
    position: absolute; left: 797px; top: 328px; width: 351px; height: 343px;
    border: 3px solid #8dbd7a;
    background: linear-gradient(135deg, #e1ead9 0%, var(--map-land) 40%, #e4e2dc 100%);
  }
  .gps { position: absolute; right: 60px; top: 684px; font-size: 13px; }
  .tagline {
    position: absolute; right: 52px; top: 740px;
    text-align: right; font-size: 22px; line-height: 30px;
  }
  .tagline em { font-style: italic; }
</style>
</head>
<body>
<div class="flyer">
  <svg class="banners" width="1200" height="846" viewBox="0 0 1200 846" aria-hidden="true">
    <defs>
      <linearGradient id="pill" x1="0" y1="0" x2="0" y2="1">
        <stop offset="0" stop-color="#7fbb6c"/>
        <stop offset="0.5" stop-color="#5c9c48"/>
        <stop offset="1" stop-color="#3f7f30"/>
      </linearGradient>
      <linearGradient id="bar" x1="0" y1="0" x2="0" y2="1">
        <stop offset="0" stop-color="#8cc678"/>
        <stop offset="1" stop-color="#4c8f3c"/>
      </linearGradient>
    </defs>
    <g>
      <rect x="790" y="37" width="355" height="18" fill="url(#bar)"/>
      <rect x="52" y="37" width="748" height="76" rx="38" fill="#2f5f25" opacity="0.35" transform="translate(2,3)"/>
      <rect x="50" y="35" width="750" height="76" rx="38" fill="url(#pill)" stroke="#c9e3bd" stroke-width="2"/>
    </g>
    <g>
      <rect x="790" y="711" width="355" height="18" fill="url(#bar)"/>
      <rect x="52" y="713" width="748" height="78" rx="39" fill="#2f5f25" opacity="0.35" transform="translate(2,3)"/>
      <rect x="50" y="711" width="750" height="78" rx="39" fill="url(#pill)" stroke="#c9e3bd" stroke-width="2"/>
    </g>
  </svg>

  <div class="banner-text top">When you need a van for business<br>purposes give Brackley a call first.</div>

  <section class="intro">
    <p>We have vans in all sizes including Luton tail lifts for short and long term rental on flexible terms for any purpose at very competitive prices.</p>
    <p>We supply vans to businesses throughout Herts and Essex from large blue chip multinationals to small self employed tradesman. We understand the requirements of business customers and provide a low cost, flexible, efficient van hire solution regardless of the size of your business.</p>
  </section>

  <section class="feature f1">
    <svg class="icon" viewBox="0 0 50 34" aria-hidden="true"><rect x="1" y="8" width="28" height="18" rx="2" fill="#6a6a6a"/><path d="M29 12h8l6 7v7H29z" fill="#6a6a6a"/><circle cx="9" cy="28" r="4" fill="#444"/><circle cx="36" cy="28" r="4" fill="#444"/><rect x="16" y="2" width="22" height="22" fill="#fff" stroke="#6a6a6a" stroke-width="2"/><path d="M19 12l6 7 14-17" fill="none" stroke="#3f8f2f" stroke-width="5" stroke-linecap="round"/></svg>
    <h2>We’re cheaper than the rest</h2>
    <p>We regularly search the market to ensure our pricing is always competitive.<br>It's important to us to give you excellent value for money.<br>We operate a clear pricing structure with no hidden extras.<br>Call us now and let us give you a quote.</p>
  </section>

  <section class="feature f2">
    <svg class="icon" viewBox="0 0 50 34" aria-hidden="true"><rect x="1" y="8" width="28" height="18" rx="2" fill="#6a6a6a"/><path d="M29 12h8l6 7v7H29z" fill="#6a6a6a"/><circle cx="9" cy="28" r="4" fill="#444"/><circle cx="36" cy="28" r="4" fill="#444"/><rect x="16" y="2" width="22" height="22" fill="#fff" stroke="#6a6a6a" stroke-width="2"/><path d="M19 12l6 7 14-17" fill="none" stroke="#3f8f2f" stroke-width="5" stroke-linecap="round"/></svg>
    <h2>Short or long term van hire</h2>
    <p>We can supply vans according to your needs from just a single days<br>rental to long term contract rental for 1 month, 6 months, a whole year or more.</p>
  </section>

  <section class="feature f3">
    <svg class="icon" viewBox="0 0 50 34" aria-hidden="true"><rect x="1" y="8" width="28" height="18" rx="2" fill="#6a6a6a"/><path d="M29 12h8l6 7v7H29z" fill="#6a6a6a"/><circle cx="9" cy="28" r="4" fill="#444"/><circle cx="36" cy="28" r="4" fill="#444"/><rect x="16" y="2" width="22" height="22" fill="#fff" stroke="#6a6a6a" stroke-width="2"/><path d="M19 12l6 7 14-17" fill="none" stroke="#3f8f2f" stroke-width="5" stroke-linecap="round"/></svg>
    <h2>Committed to Customer service</h2>
    <p>We take customer service very seriously. We want you to be delighted<br>each and every time you use us. That’s why We’ll always go out of our<br>way to give you a first class service.</p>
  </section>

  <address class="address" style="font-style:normal">
    42 Dunmore Court<br>Harlow<br>Essex<br>CM17 2QX<br><span class="phone">0800 07 316 94</span>
  </address>
  <div class="web">www.brackleyvanhire-example.com</div>

  <div class="map" role="img" aria-label="Street map of the Harlow industrial estate with a pin marking 42 Dunmore Court"></div>
  <div class="gps">GPS: +51° 47' 12.08", +0° 6' 41.35”</div>

  <div class="banner-text bottom">The longer you hire the cheaper it gets with<br>discounts of up to 70% on our daily rental rates.</div>

  <div class="tagline"><em>Affordable &amp; Flexible</em> van<br>hire solutions from Brackley</div>
</div>
</body>
</html>
```